Business card for real estate agent / office

We're looking for a new business card. We want something that is pretty clean, modern and sleek. Something that also tells people that we are a new age company...cutting edge. Although real estate has been done a certain way the last 100 years, we have energy and vibrance. Company name is Silver Meadow Properties. info can be found here: http://www.smprealtyhub.example/

needs to include: Name, title, phone number, email. our license number also needs to be displayed somewhere.

Target Market(s)

25-55 homeowners or potential homeowners

Industry/Entity Type

Business

Contact Information for Business Card

we need business card designs for real estate agent / office

Font styles to use
Serif

Requirements
Must have
• needs to include: Name, title, phone number, email. our license number also needs to be displayed somewhere and company name.
Nice to have
• placement area for photo

```html
<!DOCTYPE html>
<html lang="en">
<head>
<meta charset="utf-8">
<title>Silver Meadow Properties — Business Card</title>
<link rel="stylesheet" href="https://fonts.googleapis.com/css2?family=Source+Sans+3:wght@400;600&display=swap">
<style>
  :root {
    --stage: #0a0a0a;
    --card-white: #ffffff;
    --navy: #0b476b;
    --navy-text: #0d3a63;
    --green: #5bb946;
    --ink: #1c1c1c;
    --rule: #d5dbe0;
  }
  * { margin: 0; padding: 0; box-sizing: border-box; }
  html, body {
    width: 1200px; height: 900px; overflow: hidden;
    background: var(--stage);
    font-family: "Source Sans 3", "Myriad Pro", Arial, sans-serif;
  }
  .stage { position: relative; width: 1200px; height: 900px; }
  .card {
    position: absolute; top: 306px;
    width: 440px; height: 271px;
    border-radius: 12px;
    overflow: hidden;
  }
  .card--front { left: 149px; background: var(--card-white); }
  .card--back { left: 608px; background: var(--navy); }

  .brand {
    position: absolute; left: 18px; top: 98px; width: 204px;
    text-align: center; color: var(--navy-text);
    font-weight: 600; line-height: 1.05;
  }
  .brand__name { font-size: 29px; letter-spacing: -0.3px; }
  .brand__sub { font-size: 14px; letter-spacing: 3px; margin-top: 4px; }

  .divider {
    position: absolute; left: 233px; top: 76px;
    width: 1px; height: 128px; background: var(--rule);
  }

  .details { position: absolute; left: 250px; top: 76px; width: 184px; color: var(--ink); }
  .details__name {
    font-size: 18px; font-weight: 600; color: var(--navy-text);
    letter-spacing: 0.2px; line-height: 22px;
  }
  .details__name span { color: var(--green); }
  .details__title { font-size: 13px; line-height: 16px; white-space: nowrap; }
  .details__license { font-size: 13px; line-height: 16px; color: var(--navy-text); margin-top: 6px; margin-bottom: 6px; }
  .contact { list-style: none; font-size: 13px; line-height: 16px; }
  .contact li { display: flex; align-items: center; gap: 6px; white-space: nowrap; }
  .contact svg { width: 10px; height: 10px; fill: var(--navy-text); flex: none; }

  .back-brand {
    position: absolute; left: 0; right: 0; top: 78px;
    text-align: center; color: #ffffff; font-weight: 600; line-height: 1.1;
  }
  .back-brand__name { font-size: 34px; }
  .back-brand__sub { font-size: 15px; letter-spacing: 4px; margin-top: 4px; }
  .tagline {
    position: absolute; left: 0; right: 0; top: 207px;
    text-align: center; color: #ffffff; font-size: 15.5px; letter-spacing: 0.1px;
  }
</style>
</head>
<body>
<main class="stage">
  <section class="card card--front" aria-label="Card front">
    <div class="brand">
      <div class="brand__name">Silver Meadow</div>
      <div class="brand__sub">PROPERTIES</div>
    </div>
    <div class="divider"></div>
    <div class="details">
      <p class="details__name">DANIEL <span>HARPER</span></p>
      <p class="details__title">Real Estate Broker,Realtor,MBA</p>
      <p class="details__license">CA BRE #02917453</p>
      <ul class="contact">
        <li><svg viewBox="0 0 10 10" aria-hidden="true"><path d="M2 0.5 3.6 2.6 2.7 3.6C3.3 5 5 6.7 6.4 7.3L7.4 6.4 9.5 8 8.6 9.5C4.5 9.3 0.7 5.5 0.5 1.4Z"/></svg>310.555.0148</li>
        <li><svg viewBox="0 0 10 10" aria-hidden="true"><path d="M0.5 2h9v6h-9z M0.5 2 5 5.5 9.5 2"/></svg>dan@smprops.example</li>
        <li><svg viewBox="0 0 10 10" aria-hidden="true"><circle cx="5" cy="5" r="4.5"/></svg>www.smprops.example</li>
      </ul>
    </div>
  </section>

  <section class="card card--back" aria-label="Card back">
    <div class="back-brand">
      <div class="back-brand__name">Silver Meadow</div>
      <div class="back-brand__sub">PROPERTIES</div>
    </div>
    <p class="tagline">WE GREATLY APPRECIATE YOUR REFERRALS</p>
  </section>
</main>
</body>
</html>
```